Energieausweis
Zielgruppe
Zielgruppe sind Immobilieninteressenten - Verwendung in einem Immobilienmagazin und im Internet.
Aufgabenstellung
Ab dem 1. Mai muss in Deutschland die Energie-Effizienzklasse bei Immobilienangeboten mit veröffentlicht werden. Das kann man nüchtern in Zahlen darstellen, aber auch in einer netten Grafik. In der Anlage finden 2 von uns gekaufte Vorimka-Bilder. Das Bild mit dem Männchen ist eine sehr nette Idee. Da wir in unserem Logo auch ein Männchen haben, bietet es sich an, ein TalwiesenHof-Männchen zusammen mit der bunten Grafik zu gestalten. (Das Vorimka-Bild soll nur die Idee erklären - bitte nicht verwenden). Wenn die Grafik fertig ist, legen wir einen Pfeil zur Kennzeichnung der jeweiligen Energieklasse hinzu. Das heisst, wir haben dann für jede Energieklasse eine entsprechende Vorlage und dem richtig platzierten Pfeil. Weiter finden sie in der Anlage unser Firmenlogo zur freuen Verwendung.

```html
<!DOCTYPE html>
<html lang="de">
<head>
<meta charset="utf-8">
<title>Energieausweis – Berechneter Energiebedarf</title>
<link rel="stylesheet" href="https://fonts.googleapis.com/css2?family=Barlow:wght@600;700;800&display=swap">
<style>
  :root {
    --brand-blue: #0f5294;
    --brand-red: #e3353b;
    --roof-grey: #dcdcde;
    --track-grey: #f3f3f3;
    --paper: #ffffff;
    --class-a: #007a3d;
    --class-b: #2ea43c;
    --class-c: #96c150;
    --class-d: #e5dd00;
    --class-e: #fbbc05;
    --class-f: #ea6e3a;
    --class-g: #e3353b;
  }
  html, body {
    margin: 0;
    padding: 0;
    width: 848px;
    height: 1200px;
    overflow: hidden;
    background: var(--paper);
  }
  .energy-label {
    display: block;
    width: 848px;
    height: 1200px;
    font-family: "Barlow", "Arial Narrow", sans-serif;
  }
  .roof-sky { fill: var(--roof-grey); }
  .house-frame { fill: var(--brand-blue); }
  .house-inner { fill: var(--paper); }
  .roof-edge { fill: none; stroke: var(--paper); stroke-width: 4; }
  .title { font-size: 68px; font-weight: 700; }
  .title-energie { fill: var(--brand-red); }
  .title-ausweis { fill: var(--brand-blue); }
  .subtitle { fill: var(--brand-blue); font-size: 40px; font-weight: 700; }
  .track { fill: var(--track-grey); }
  .class-letter { fill: var(--paper); font-size: 46px; font-weight: 800; }
  .class-arrow { stroke: var(--paper); stroke-width: 3; stroke-linejoin: round; }
  .marker { stroke: var(--paper); stroke-width: 3; stroke-linejoin: round; }
  .marker-figure { fill: rgba(255,255,255,0.35); }
  .brand-dot { fill: var(--brand-blue); }
  .brand-name { fill: var(--brand-blue); font-size: 36px; font-weight: 700; }
</style>
</head>
<body>
<svg class="energy-label" viewBox="0 0 848 1200" xmlns="http://www.w3.org/2000/svg">
  <!-- roof -->
  <rect class="roof-sky" x="81" y="75" width="685" height="160"/>
  <polygon class="house-frame" points="81,229 424,113 766,229 766,266 424,152 81,266"/>
  <polygon class="house-inner" points="81,266 424,152 766,266 766,374 81,374"/>
  <polyline class="roof-edge" points="81,227 424,111 766,227"/>

  <!-- walls -->
  <rect class="house-frame" x="81" y="374" width="685" height="606"/>
  <rect class="house-inner" x="116" y="374" width="616" height="571"/>

  <!-- heading -->
  <text class="title" x="151" y="310" textLength="545" lengthAdjust="spacingAndGlyphs"><tspan class="title-energie">Energie</tspan><tspan class="title-ausweis">Ausweis</tspan></text>
  <text class="subtitle" x="151" y="352" textLength="545" lengthAdjust="spacingAndGlyphs">Berechneter Energiebedarf</text>

  <!-- scale tracks -->
  <g class="tracks">
    <rect class="track" x="152" y="374" width="545" height="60" rx="3"/>
    <rect class="track" x="152" y="441" width="545" height="60" rx="3"/>
    <rect class="track" x="152" y="508" width="545" height="60" rx="3"/>
    <rect class="track" x="152" y="575" width="545" height="60" rx="3"/>
    <rect class="track" x="152" y="642" width="545" height="60" rx="3"/>
    <rect class="track" x="152" y="709" width="545" height="60" rx="3"/>
    <rect class="track" x="152" y="776" width="545" height="60" rx="3"/>
  </g>

  <!-- efficiency classes -->
  <g class="classes">
    <path class="class-arrow" style="fill:var(--class-a)" d="M152,377 q0,-3 3,-3 H330 L367,404 L330,434 H155 q-3,0 -3,-3 Z"/>
    <text class="class-letter" x="181" y="421">A</text>
    <path class="class-arrow" style="fill:var(--class-b)" d="M152,444 q0,-3 3,-3 H360 L397,471 L360,501 H155 q-3,0 -3,-3 Z"/>
    <text class="class-letter" x="181" y="488">B</text>
    <path class="class-arrow" style="fill:var(--class-c)" d="M152,511 q0,-3 3,-3 H391 L428,538 L391,568 H155 q-3,0 -3,-3 Z"/>
    <text class="class-letter" x="181" y="555">C</text>
    <path class="class-arrow" style="fill:var(--class-d)" d="M152,578 q0,-3 3,-3 H421 L458,605 L421,635 H155 q-3,0 -3,-3 Z"/>
    <text class="class-letter" x="181" y="622">D</text>
    <path class="class-arrow" style="fill:var(--class-e)" d="M152,645 q0,-3 3,-3 H451 L488,672 L451,702 H155 q-3,0 -3,-3 Z"/>
    <text class="class-letter" x="181" y="689">E</text>
    <path class="class-arrow" style="fill:var(--class-f)" d="M152,712 q0,-3 3,-3 H481 L518,739 L481,769 H155 q-3,0 -3,-3 Z"/>
    <text class="class-letter" x="181" y="756">F</text>
    <path class="class-arrow" style="fill:var(--class-g)" d="M152,779 q0,-3 3,-3 H511 L548,806 L511,836 H155 q-3,0 -3,-3 Z"/>
    <text class="class-letter" x="181" y="823">G</text>
  </g>

  <!-- class markers -->
  <g class="marker-a">
    <path class="marker" style="fill:var(--class-a)" d="M552,404 L589,374 H694 q3,0 3,3 V431 q0,3 -3,3 H589 Z"/>
    <rect class="marker-figure" x="590" y="376" width="70" height="56" rx="6" role="img" aria-label="Maskottchen mit Haus in den Armen"/>
  </g>
  <g class="marker-e">
    <path class="marker" style="fill:var(--class-e)" d="M552,672 L589,642 H694 q3,0 3,3 V699 q0,3 -3,3 H589 Z"/>
    <rect class="marker-figure" x="590" y="644" width="70" height="56" rx="6" role="img" aria-label="Maskottchen mit Haus in den Armen"/>
  </g>

  <!-- brand -->
  <g class="brand">
    <rect class="brand-dot" x="300" y="886" width="26" height="26"/>
    <text class="brand-name" x="338" y="912">TalwiesenHof</text>
  </g>
</svg>
</body>
</html>
```